Tollo is the place for Used Car Inspections

Tollo ONLY sells Used Car Inspections.

We need a website that tells that story simply.

Please be original and don't just copy my mockup. I'm not a designer.

Reason: Too few designers(<10)...too many weak designs(>80). I have subsequently revised my brief, uploaded more defined mockup and have tried to inspire some originality. I have also invited add designs, some who have declined. Any suggestions. Any suggestions?

Reason: Still waiting on original designs

Target Market(s)

Car Buyers

Industry/Entity Type

Used Car

Logo Text

Tollo

Number of Pages Required

5+ page

Font styles to use
Sans Serif

Colors
33a6d7
ffc214

Requirements
Must have
• Why Tollo?
• -Top 5 Questions
• Tollo Certified
• -Graphic detailing inspection
• How it Works
• -Graphic-- 1. Find a Location 2. Personal/Vehicle Info Form 3. Purchase
• -Get a Tollo Inspection
• Get a Tollo Inspection
• -Find a Location
• -Personal/Vehicle info Form
• -Purchase
• Become a Tollo Dealer
• -Form
• -Upload Credentials
• About Us
• Contact Us
• Term & Conditions
• Privacy
• FAQ
• Press
• Social Media
Nice to have
• Customer feedback-Quorra
Should not have
• Not sure

```html
<!DOCTYPE html>
<html lang="en">
<head>
<meta charset="utf-8">
<title>Tollo — The Used Car Inspection</title>
<link rel="stylesheet" href="https://fonts.googleapis.com/css2?family=Open+Sans:wght@400;600;700;800&family=Roboto+Slab:wght@700&display=swap">
<style>
:root{
  --blue:#33a6d7;
  --blue-dark:#1f86b4;
  --yellow:#ffc214;
  --ink:#2a2a2a;
  --muted:#6b6b6b;
  --night:#1f2124;
  --night-2:#2c2f33;
  --line:#d9d9d9;
  --paper:#ffffff;
}
*{box-sizing:border-box;margin:0;padding:0}
html,body{width:1200px;height:2312px;overflow:hidden}
body{font-family:"Open Sans",Arial,sans-serif;color:var(--ink);background:var(--paper);position:relative}
.wrap{width:880px;margin:0 auto;position:relative}

/* header */
.site-header{height:76px;position:relative;background:#fff}
.brand{position:absolute;left:28px;top:14px;display:flex;align-items:center;gap:8px;font-weight:800;font-size:22px;color:var(--blue)}
.brand-dot{width:26px;height:26px;border-radius:50%;background:var(--yellow)}
.util-links{position:absolute;right:120px;top:6px;font-size:10px;color:var(--muted);display:flex;gap:14px}
.main-nav{position:absolute;left:400px;top:38px;width:680px;height:30px;background:var(--blue);display:flex;justify-content:space-around;align-items:center}
.main-nav a{color:#fff;text-decoration:none;font-size:11px;font-weight:700;letter-spacing:.5px;padding:5px 8px}
.main-nav a.is-active{background:var(--yellow);color:var(--ink)}

/* hero */
.hero{width:880px;height:364px;margin:0 auto;position:relative;overflow:hidden}
.hero-photo{position:absolute;inset:0;background:linear-gradient(180deg,#8c9aa6 0%,#5d6a75 45%,#3c454d 100%)}
.hero-copy{position:absolute;inset:0;text-align:center;color:#fff}
.hero-kicker{position:absolute;left:0;right:0;top:24px;font-size:40px;font-weight:800;line-height:1}
.hero-title{position:absolute;left:0;right:0;top:72px;font-size:58px;font-weight:800;line-height:1}
.hero-cta{position:absolute;left:260px;top:148px;width:320px;height:48px;background:var(--yellow);color:var(--ink);font-size:24px;font-weight:700;line-height:48px;border-radius:3px}
.hero-note{position:absolute;left:0;right:0;top:222px;font-size:19px;font-style:italic;font-weight:600;line-height:1.25}
.hero-tag{position:absolute;left:0;right:0;bottom:18px;font-size:40px;font-weight:800}

/* welcome */
.welcome{margin:32px auto 0;width:880px;height:200px;display:flex;gap:24px}
.welcome-photo{width:200px;height:200px;background:linear-gradient(135deg,#c9b79e,#7e6c58)}
.welcome-box{flex:1;border:1px solid var(--line);border-left:4px solid var(--yellow);padding:22px 26px}
.welcome-box h2{color:var(--blue);font-size:22px;font-weight:600;margin-bottom:12px}
.welcome-box p{font-size:12px;line-height:1.6;color:var(--muted);margin-bottom:8px}

/* why */
.why{margin-top:38px;text-align:center}
.section-title{font-family:"Roboto Slab",Georgia,serif;font-size:38px;color:var(--ink)}
.why-grid{width:880px;margin:18px auto 0;display:grid;grid-template-columns:1fr 60px 1fr;text-align:left;row-gap:14px}
.why-col-head{font-size:26px;color:var(--ink);padding-left:10px}
.flag-pill{height:42px;border:1px solid #bfbfbf;border-radius:6px;display:flex;align-items:center;padding-left:18px;font-size:15px;color:var(--ink);box-shadow:0 2px 3px rgba(0,0,0,.08)}
.flag-pill::before{content:"➜";font-size:12px;margin-right:14px;color:var(--ink)}
.why-icon{display:flex;align-items:center;justify-content:center}

/* certified */
.certified{margin-top:36px;height:352px;background:linear-gradient(180deg,var(--night-2),var(--night));color:#fff;position:relative}
.certified .section-title{color:#fff;text-align:center;padding-top:24px}
.certified-art{position:absolute;left:230px;top:92px;width:240px;height:230px;border-radius:50%;background:radial-gradient(circle,#f2a93b 0%,#3a8fc4 55%,#2c2f33 72%)}
.certified-list{position:absolute;left:636px;top:96px;width:340px}
.certified-list h3{font-family:"Roboto Slab",Georgia,serif;font-size:19px;margin-bottom:2px}
.certified-list p{font-size:11px;line-height:1.45;color:#cfcfcf;margin-bottom:14px}
.btn-outline{display:inline-block;border:1px solid #fff;font-size:11px;padding:5px 12px;color:#fff}

/* services */
.services{width:880px;margin:34px auto 0;display:grid;grid-template-columns:repeat(5,1fr);gap:14px;height:408px}
.service{border:1px solid var(--line);text-align:center;padding:16px 12px;position:relative}
.service h4{font-size:14px;font-weight:700;line-height:1.3;height:40px}
.service svg{margin:16px auto 18px;display:block}
.service p{font-size:11px;line-height:1.6;color:var(--muted)}
.btn-learn{position:absolute;left:50%;transform:translateX(-50%);bottom:22px;background:var(--yellow);font-size:10px;font-weight:700;padding:6px 16px;color:var(--ink)}

/* testimonial */
.testimonial{margin-top:28px;height:240px;background:linear-gradient(90deg,#26292c,#3d4247 60%,#2a2d31);color:#fff;position:relative}
.testimonial-photo{position:absolute;left:200px;top:44px;width:116px;height:140px;background:linear-gradient(180deg,#b9c3cc,#6d7985);border:3px solid #fff}
.testimonial-body{position:absolute;left:348px;top:40px;width:620px}
.testimonial-body h3{font-size:26px;font-weight:400;margin-bottom:10px}
.testimonial-body p{font-size:20px;line-height:1.4}
.testimonial-name{position:absolute;left:348px;top:196px;font-size:13px;color:#ddd}

/* footer */
.site-footer{height:180px;background:#111214;color:#fff}
.footer-grid{width:880px;margin:0 auto;display:grid;grid-template-columns:180px 200px 280px 220px;padding-top:24px}
.footer-grid h5{font-size:17px;font-weight:600;margin-bottom:10px}
.footer-grid li{list-style:none;font-size:11px;color:#cfcfcf;line-height:1.65;display:flex;align-items:center;gap:8px}
.social-dot{width:10px;height:10px;border-radius:2px;background:var(--blue)}
.footer-grid p{font-size:11px;color:#cfcfcf;line-height:1.5}
.subscribe-field{margin-top:10px;width:220px;height:22px;background:#fff}
.subscribe-btn{margin-top:8px;display:inline-block;background:var(--yellow);color:var(--ink);font-size:10px;font-weight:700;padding:4px 12px}
.copyright{height:32px;background:var(--blue);color:#fff;font-size:11px;text-align:center;line-height:32px}
</style>
</head>
<body>

<header class="site-header">
  <div class="brand"><span class="brand-dot"></span>Tollo</div>
  <div class="util-links"><span>Get Inspection</span><span>Become a Dealer</span></div>
  <nav class="main-nav">
    <a href="#">HOME</a>
    <a href="#">ABOUT US</a>
    <a href="#" class="is-active">TOLLO CERTIFIED</a>
    <a href="#">HOW IT WORKS</a>
    <a href="#">FAQS</a>
    <a href="#">CONTACT US</a>
  </nav>
</header>

<section class="hero">
  <div class="hero-photo" role="img" aria-label="Row of used cars parked at a dealership lot"></div>
  <div class="hero-copy">
    <div class="hero-kicker">Trusted Sellers...</div>
    <div class="hero-title">Smart Buyers</div>
    <div class="hero-cta">Get a Tollo Inspection</div>
    <div class="hero-note">*Free AutoTrace Vehicle History Report<br>with every inspection</div>
    <div class="hero-tag">The Original Used Car Inspection</div>
  </div>
</section>

<section class="welcome">
  <div class="welcome-photo" role="img" aria-label="Couple sitting inside a car they are inspecting"></div>
  <div class="welcome-box">
    <h2>Welcome To Our Site</h2>
    <p>Tollo is the place for used car inspections. We bring trained mechanics, clear reports and honest advice together so buyers and sellers can agree on a fair price with confidence before any money changes hands.</p>
    <p>Every inspection covers the engine, body, brakes and electrics, and comes with a full vehicle history report at no extra cost.</p>
  </div>
</section>

<section class="why">
  <h2 class="section-title">Why buy a Tollo Inspection?</h2>
  <div class="why-grid">
    <div class="why-col-head">Buyers</div><div></div><div class="why-col-head">Sellers</div>

    <div class="flag-pill">See the red flags before you buy.</div>
    <div class="why-icon"><svg width="26" height="16" viewBox="0 0 26 16"><path d="M3 9 L7 3 H19 L23 9 V13 H3 Z" fill="#ffc214"/><circle cx="8" cy="13" r="2.5" fill="#2a2a2a"/><circle cx="18" cy="13" r="2.5" fill="#2a2a2a"/></svg></div>
    <div class="flag-pill">See the red flags before you buy.</div>

    <div class="flag-pill">See the red flags before you buy.</div>
    <div class="why-icon"><svg width="26" height="16" viewBox="0 0 26 16"><path d="M3 9 L7 3 H19 L23 9 V13 H3 Z" fill="#ffc214"/><circle cx="8" cy="13" r="2.5" fill="#2a2a2a"/><circle cx="18" cy="13" r="2.5" fill="#2a2a2a"/></svg></div>
    <div class="flag-pill">See the red flags before you buy.</div>

    <div class="flag-pill">See the red flags before you buy.</div>
    <div class="why-icon"><svg width="26" height="16" viewBox="0 0 26 16"><path d="M3 9 L7 3 H19 L23 9 V13 H3 Z" fill="#ffc214"/><circle cx="8" cy="13" r="2.5" fill="#2a2a2a"/><circle cx="18" cy="13" r="2.5" fill="#2a2a2a"/></svg></div>
    <div class="flag-pill">See the red flags before you buy.</div>
  </div>
</section>

<section class="certified">
  <h2 class="section-title">What is Tollo Certified?</h2>
  <div class="certified-art" role="img" aria-label="Gear and wrench illustration representing the inspection process"></div>
  <div class="certified-list">
    <h3>Certified Mechanics</h3>
    <p>All mechanics are industry professionals certified by Tollo and trusted by the local community.</p>
    <h3>Car Inspection</h3>
    <p>Our 150-point inspection gives your seller a clear, honest report so you can accurately determine the true condition of the car you want.</p>
    <h3>AutoTrace</h3>
    <p>Our free history check reveals ownership, accidents and mileage so there are no surprises later.</p>
    <span class="btn-outline">View Our Details</span>
  </div>
</section>

<section class="services">
  <div class="service">
    <h4>Car Park &amp;<br>Traffic Control</h4>
    <svg width="60" height="60" viewBox="0 0 60 60"><path d="M30 6 L44 50 H16 Z" fill="none" stroke="#33a6d7" stroke-width="3"/><line x1="22" y1="32" x2="38" y2="32" stroke="#33a6d7" stroke-width="3"/><line x1="10" y1="52" x2="50" y2="52" stroke="#33a6d7" stroke-width="3"/></svg>
    <p>On the other hand, we denounce with righteous indignation and dislike men who are so beguiled and demoralized.</p>
    <span class="btn-learn">LEARN MORE</span>
  </div>
  <div class="service">
    <h4>Property Protection</h4>
    <svg width="60" height="60" viewBox="0 0 60 60"><path d="M30 6 L50 14 V30 C50 42 40 50 30 54 C20 50 10 42 10 30 V14 Z" fill="none" stroke="#33a6d7" stroke-width="3"/><path d="M21 30 L28 37 L40 24" fill="none" stroke="#33a6d7" stroke-width="3"/></svg>
    <p>On the other hand, we denounce with righteous indignation and dislike men who are so beguiled and demoralized.</p>
    <span class="btn-learn">LEARN MORE</span>
  </div>
  <div class="service">
    <h4>Pedestrian<br>Control Systems</h4>
    <svg width="60" height="60" viewBox="0 0 60 60"><circle cx="30" cy="10" r="5" fill="#33a6d7"/><path d="M30 17 V36 M30 36 L22 52 M30 36 L38 52 M20 26 H40" stroke="#33a6d7" stroke-width="3" fill="none"/></svg>
    <p>On the other hand, we denounce with righteous indignation and dislike men who are so beguiled and demoralized.</p>
    <span class="btn-learn">LEARN MORE</span>
  </div>
  <div class="service">
    <h4>Floor Safety &amp;<br>Cable Protection</h4>
    <svg width="60" height="60" viewBox="0 0 60 60"><path d="M18 52 L24 8 H36 L42 52" fill="none" stroke="#33a6d7" stroke-width="3"/><path d="M30 18 L36 32 H24 Z" fill="#33a6d7"/></svg>
    <p>On the other hand, we denounce with righteous indignation and dislike men who are so beguiled and demoralized.</p>
    <span class="btn-learn">LEARN MORE</span>
  </div>
  <div class="service">
    <h4>Signage</h4>
    <svg width="60" height="60" viewBox="0 0 60 60"><line x1="30" y1="6" x2="30" y2="54" stroke="#33a6d7" stroke-width="3"/><path d="M14 14 H44 L50 20 L44 26 H14 Z" fill="none" stroke="#33a6d7" stroke-width="3"/><path d="M46 32 H16 L10 38 L16 44 H46 Z" fill="none" stroke="#33a6d7" stroke-width="3"/></svg>
    <p>On the other hand, we denounce with righteous indignation and dislike men who are so beguiled and demoralized.</p>
    <span class="btn-learn">LEARN MORE</span>
  </div>
</section>

<section class="testimonial">
  <div class="testimonial-photo" role="img" aria-label="Portrait of a satisfied customer"></div>
  <div class="testimonial-body">
    <h3>Testimonials</h3>
    <p>Lorem Ipsum is simply dummy text of the printing and typesetting industry. Lorem Ipsum has been the industry's standard dummy text ever since the 1500s, when an unknown printer took a galley</p>
  </div>
  <div class="testimonial-name">Mr Harlow</div>
</section>

<footer class="site-footer">
  <div class="footer-grid">
    <div>
      <h5>Company</h5>
      <ul><li>About</li><li>Testimonials</li><li>Customer service</li><li>Contact Us</li></ul>
    </div>
    <div>
      <h5>Connect with Us</h5>
      <ul><li><span class="social-dot"></span>Facelink</li><li><span class="social-dot"></span>Chatterly</li><li><span class="social-dot"></span>CirclePlus</li></ul>
    </div>
    <div>
      <h5>Subscribe to Our Newsletter</h5>
      <p>Get new inspection reports and dealer news.</p>
      <div class="subscribe-field"></div>
      <span class="subscribe-btn">SUBSCRIBE</span>
    </div>
    <div>
      <h5>Contact Us</h5>
      <ul><li>Phone: 0800 555 014</li><li>Fax: 04 555 0192</li><li>Email: info@tollo-inspect.example</li></ul>
    </div>
  </div>
</footer>
<div class="copyright">Copyright © 2016 Tollo. All rights reserved.</div>

</body>
</html>
```